Brume vodka

With the logo attached in the subsequent file, a business card that reflects a premium and organic vodka. On the first side, the company logo in large. The names must be included on the back of the card (Miguel Ángel Tomás Ferrandis with the number +34 655 271 389 and Pau Berenguer Casals and +34 677 314 920). The slogan "What binds us" and "Organic and permium vodka" in bold E-mail (brumevodka@mailfield.net); Website www.brumevodkaorg.net

```html
<!DOCTYPE html>
<html lang="en">
<head>
<meta charset="utf-8">
<title>Brume Vodka – Business Card</title>
<link rel="stylesheet" href="https://fonts.googleapis.com/css2?family=EB+Garamond:wght@400;600&display=swap">
<style>
  :root {
    --backdrop: #eeeeee;
    --card-front: #ffffff;
    --card-back: #1f1f1f;
    --brand-grey: #7b7b7b;
    --ink-light: #f4f4f4;
    --ink-soft: #bdbdbd;
    --rule: #8a8a8a;
  }
  * { margin: 0; padding: 0; box-sizing: border-box; }
  html, body {
    width: 1200px;
    height: 757px;
    overflow: hidden;
    background: var(--backdrop);
    font-family: "EB Garamond", Georgia, serif;
  }
  .canvas {
    position: relative;
    width: 1200px;
    height: 757px;
  }
  .card {
    position: absolute;
    top: 95px;
    width: 299px;
    height: 498px;
  }
  .card--front {
    left: 190px;
    background: var(--card-front);
  }
  .card--back {
    left: 683px;
    background: var(--card-back);
    color: var(--ink-light);
    text-align: center;
  }

  /* Front: brand name */
  .brand {
    position: absolute;
    left: 0;
    right: 0;
    top: 168px;
    text-align: center;
    color: var(--brand-grey);
    font-weight: 400;
  }
  .brand__name {
    display: block;
    font-size: 68px;
    line-height: 1;
    letter-spacing: 1px;
    text-transform: uppercase;
  }
  .brand__type {
    display: block;
    margin-top: 4px;
    font-size: 16px;
    letter-spacing: 4px;
    text-transform: uppercase;
  }

  /* Back: contacts */
  .contact {
    position: absolute;
    left: 0;
    right: 0;
    line-height: 1;
  }
  .contact__name {
    font-size: 15px;
    text-transform: uppercase;
    letter-spacing: 0.2px;
  }
  .contact__phone {
    font-size: 15px;
    margin-top: 2px;
  }
  .contact--first { top: 85px; }
  .contact--second { top: 139px; }
  .divider {
    position: absolute;
    top: 128px;
    left: 16px;
    right: 16px;
    height: 1px;
    background: var(--rule);
  }
  .web-details {
    position: absolute;
    left: 0;
    right: 0;
    top: 208px;
    font-size: 18px;
    line-height: 28px;
  }
  .slogans {
    position: absolute;
    left: 0;
    right: 0;
    top: 290px;
    font-weight: 600;
    line-height: 1.3;
  }
  .slogans__tagline {
    font-size: 17px;
    color: var(--ink-light);
  }
  .slogans__claim {
    font-size: 14px;
    color: var(--ink-soft);
    letter-spacing: 0.3px;
  }
</style>
</head>
<body>
  <main class="canvas">
    <section class="card card--front" aria-label="Card front">
      <div class="brand">
        <span class="brand__name">Brume</span>
        <span class="brand__type">Vodka</span>
      </div>
    </section>

    <section class="card card--back" aria-label="Card back">
      <div class="contact contact--first">
        <p class="contact__name">Miguel Ángel Tomás Ferrandis</p>
        <p class="contact__phone">+34 655 271 389</p>
      </div>
      <div class="divider"></div>
      <div class="contact contact--second">
        <p class="contact__name">Pau Berenguer Casals</p>
        <p class="contact__phone">+34 677 314 920</p>
      </div>
      <div class="web-details">
        <p class="web-details__email">brumevodka@mailfield.net</p>
        <p class="web-details__site">www.brumevodkaorg.net</p>
      </div>
      <div class="slogans">
        <p class="slogans__tagline">What binds us</p>
        <p class="slogans__claim">Organic and premium vodka</p>
      </div>
    </section>
  </main>
</body>
</html>
```